Restaurant Email Club Sign Up Poster

Looking for a creative design that will catch people's eye and prompt them to sign up for our email club for our Restaurant that we run in Omaha, Nebraska. Open to any creative ways to most effectively grab peoples attention quickly without being too confusing. Want it to be simple but actionable.

Have attached some documents for your assistance - in addition to some marketing materials we have put out in the past.

Would like to put design on posters to hang up throughout the restaurant and likely will make stickers to put on check presenters as well.

Catchy stock photo or use of the cheese curd photo probably good idea - callout things mentioned in the "must haves" section below. Looking for most creative and catchy, yet simple design.

Target Market(s)

30-50 year olds males and females.

Industry/Entity Type

Restaurant

Requirements
Must have
• Must include callouts for -
• Sign up for E-Club for access to future offers and events (or something along these lines)
• Free Appetizer for Signing Up
• Free Birthday Meal
Should not have
• Please do not make this poster like the postcard that I attached to the project - this is not a poster to call out that we are a new burger and beer spot, that we have 40 rotating taps, or that we have 15 specialty burgers, etc. This is simply a poster to grab someones attention and get them to sign up for our email club. Should maybe have a catchy question, something like, "Want a Free Appetizer?" or something catchy and similar, and then below say "And access to future deals and event happenings?"

```html
<!DOCTYPE html>
<html lang="en">
<head>
<meta charset="utf-8">
<title>E-Club Sign Up Poster</title>
<link rel="stylesheet" href="https://fonts.googleapis.com/css2?family=Lato:wght@400;700&family=Chewy&display=swap">
<style>
  :root {
    --slate: #1c1c1d;
    --slate-deep: #0f0f10;
    --white: #ffffff;
    --red: #e3242f;
    --lime: #b9d86a;
    --photo-green: #7d9a4a;
    --photo-brown: #5a3a25;
    --photo-cream: #d9d4c6;
    --icon-pink: #f26d6d;
    --icon-yellow: #f6c945;
    --icon-teal: #5fb6b0;
  }
  * { margin: 0; padding: 0; box-sizing: border-box; }
  html, body { width: 900px; height: 1200px; overflow: hidden; background: var(--slate); }
  .poster {
    position: relative; width: 900px; height: 1200px; overflow: hidden;
    background: linear-gradient(90deg, var(--slate) 0 715px, var(--slate-deep) 715px 900px);
    font-family: "Lato", Arial, sans-serif; color: var(--white);
  }
  .food-photo {
    position: absolute; left: 0; top: 0; width: 360px; height: 1200px;
    background: linear-gradient(180deg,
      var(--photo-green) 0%, var(--photo-brown) 22%,
      #b98a86 30%, var(--photo-brown) 50%,
      var(--photo-green) 62%, var(--photo-cream) 75%, var(--photo-brown) 88%, var(--photo-green) 100%);
    opacity: .55;
    -webkit-mask-image: linear-gradient(90deg, #000 70%, transparent);
            mask-image: linear-gradient(90deg, #000 70%, transparent);
  }
  .content { position: absolute; left: 360px; right: 0; top: 0; bottom: 0; text-align: center; }
  .kicker {
    position: absolute; left: 0; right: 0; top: 42px;
    font-size: 30px; letter-spacing: .36em; font-weight: 400; padding-left: 20px;
  }
  .headline {
    position: absolute; left: 0; right: 0; top: 112px;
    font-family: "Chewy", "Comic Sans MS", cursive; font-weight: 400;
    font-size: 84px; line-height: 104px; color: var(--red);
  }
  .headline .free { color: var(--lime); }
  .pitch {
    position: absolute; left: 20px; right: 20px; top: 348px;
    font-size: 31px; line-height: 50px; font-weight: 700; text-transform: uppercase;
  }
  .pitch svg { vertical-align: -10px; }
  .perk {
    position: absolute; border-top: 2px solid var(--white); border-bottom: 2px solid var(--white);
    font-size: 31px; line-height: 38px; text-transform: uppercase; font-weight: 400;
  }
  .perk--appetizer { left: 110px; width: 278px; top: 700px; padding: 18px 0 17px; }
  .perk--birthday { left: 67px; width: 363px; top: 884px; padding: 14px 0 16px; }
  .perk-icon { position: absolute; left: 50%; transform: translateX(-50%); }
  .brand {
    position: absolute; left: 0; right: 0; top: 1052px;
    display: flex; justify-content: center; align-items: center; gap: 14px;
    font-size: 30px; font-weight: 700;
  }
  .brand-dot { width: 36px; height: 36px; border-radius: 50%; background: var(--red); }
</style>
</head>
<body>
<main class="poster">
  <div class="food-photo" role="img" aria-label="Overhead photo of open-faced rye toasts topped with cream cheese, avocado, radish, spinach and cucumber on dark slate"></div>

  <section class="content">
    <p class="kicker">JOIN OUR E-CLUB</p>
    <h1 class="headline">get a <span class="free">FREE</span><br>appetizer</h1>

    <p class="pitch">
      Sign up for our e-club<br>
      <svg width="56" height="48" viewBox="0 0 56 48" aria-hidden="true">
        <ellipse cx="14" cy="14" rx="10" ry="12" fill="var(--icon-teal)"/>
        <ellipse cx="42" cy="14" rx="10" ry="12" fill="var(--icon-yellow)"/>
        <ellipse cx="28" cy="12" rx="11" ry="12" fill="var(--icon-pink)"/>
        <path d="M14 26 L16 46 M28 24 L28 46 M42 26 L40 46" stroke="#333" stroke-width="2" fill="none"/>
      </svg>
      to gain access to
      <svg width="42" height="44" viewBox="0 0 42 44" aria-hidden="true">
        <path d="M20 6 L38 40 L4 40 Z" fill="var(--icon-yellow)" stroke="#333" stroke-width="2"/>
        <circle cx="20" cy="5" r="4" fill="var(--icon-pink)"/>
        <circle cx="18" cy="26" r="3" fill="var(--icon-teal)"/><circle cx="26" cy="34" r="3" fill="var(--icon-pink)"/>
      </svg><br>
      information about<br>
      future offers and<br>
      exclusive events.
    </p>

    <svg class="perk-icon" style="top:640px" width="52" height="52" viewBox="0 0 52 52" aria-hidden="true">
      <path d="M10 22 Q8 6 26 6 Q44 6 42 22 Z" fill="var(--icon-pink)"/>
      <path d="M20 8 Q34 4 42 20 L24 20 Z" fill="var(--icon-yellow)"/>
      <path d="M8 24 H44 L40 46 H12 Z" fill="var(--icon-teal)" stroke="#333" stroke-width="2"/>
    </svg>
    <p class="perk perk--appetizer">Free appetizer<br>for signing up</p>

    <svg class="perk-icon" style="top:826px" width="52" height="50" viewBox="0 0 52 50" aria-hidden="true">
      <rect x="24" y="4" width="4" height="14" fill="var(--icon-teal)"/>
      <path d="M26 0 Q30 4 26 6 Q22 4 26 0Z" fill="var(--icon-yellow)"/>
      <rect x="6" y="20" width="40" height="12" fill="var(--icon-pink)" stroke="#333" stroke-width="2"/>
      <rect x="6" y="32" width="40" height="12" fill="var(--icon-yellow)" stroke="#333" stroke-width="2"/>
      <rect x="2" y="44" width="48" height="4" fill="#333"/>
    </svg>
    <p class="perk perk--birthday">Free birthday meal</p>

    <div class="brand"><span class="brand-dot"></span><span>Fieldhouse Grill</span></div>
  </section>
</main>
</body>
</html>
```